Website Design for Business Law Firm

We have a logo and now we would like a web site design for our new website. Our small firm provides creative and aggressive transactional (not litigation) legal services to advise healthcare, technology, internet-based and traditional companies and investors in such companies on healthcare, technology, financing, mergers/acquisitions, real estate and other transactions, legal compliance and general corporate and business matters.

We would like to see a website design that is professional and appropriate for executives, professionals, investors and government regulators to visit, that conveys professionalism and competence while being a little edgy and modern - no typical legal motifs such as gavels, books, or scales of justice. We advise businesses and investors and guide them through complicated issues quickly, capably and differently from other law firms. We are part of the business team and get things done.

The logo is attached, and we like gray as a color to complement it. The intention of the logo is to convey that in a storm or challenging time, people come to this firm, and people come to this firm when they need the power and disruption to change things or shake them up.

I have also enclosed a picture of our business card for consideration.

On the other hand, you can check out the current simple site at www.venhollow.example to see we have used a space motif in the past to evoke that we help create stars (the nebula featured there). This is not a necessary part of the new website and it may look better without it.

We appreciate your creativity and look forward to designs.

Industry/Entity Type

Business

Requirements
Must have
• We anticipate the following pages, and you may submit different ideas for the different pages:
• 1. Landing page
• 2. Services pages - healthcare, IT/Technology, general counsel services, financings, mergers/acquisitions, mediation/arbitration, procurement and productization
• 3. About Us including contact information
• Our name and contact information:
• Quellane Law Firm, P.C.
• 8716 SW 19th Ave.
• Portland, OR 97213
• phone: 971.555.0143
• fax: 971.555.0187
Nice to have
• Please consider designs that enhance the impressions we are looking for
Should not have
• Please no gavels, scales of justice, law books, or similar traditional legal imagery.

```html
<!DOCTYPE html>
<html lang="en">
<head>
<meta charset="utf-8">
<title>Quellane Law Firm – Home</title>
<link href="https://fonts.googleapis.com/css2?family=Open+Sans:wght@600&family=PT+Sans+Narrow:wght@400;700&family=Source+Sans+3:ital,wght@0,400;0,600;1,400&display=swap" rel="stylesheet">
<style>
  :root {
    --orange: #f47a0e;
    --orange-dark: #e0650a;
    --peach: #fdeadb;
    --peach-light: #fff4ec;
    --text: #6f6f6f;
    --text-dark: #2b2b2b;
    --rule: #d9d2cc;
    --footer: #2f2f2f;
    --footer-top: #4a4a4a;
    --footer-text: #c8c8c8;
    --white: #ffffff;
  }
  * { box-sizing: border-box; margin: 0; padding: 0; }
  html, body { width: 1200px; height: 1149px; overflow: hidden; background: var(--white); }
  body { position: relative; font-family: "Source Sans 3", Arial, sans-serif; color: var(--text); }
  a { color: inherit; text-decoration: none; }

  .search { position: absolute; left: 879px; top: 11px; width: 230px; height: 38px; border: 1px solid #cfcfcf; border-radius: 4px; background: var(--white); box-shadow: inset 0 1px 3px rgba(0,0,0,.08); font-size: 11px; color: #555; padding: 12px 0 0 16px; }
  .search svg { position: absolute; right: 12px; top: 9px; }

  .brand { position: absolute; left: 90px; top: 47px; height: 80px; display: flex; align-items: center; gap: 14px; }
  .brand-mark { width: 22px; height: 22px; background: var(--text-dark); }
  .brand-name { font-weight: 400; font-size: 50px; letter-spacing: 10px; color: var(--text-dark); }

  .main-nav { position: absolute; top: 84px; left: 0; font-size: 21px; color: var(--orange); }
  .main-nav a { position: absolute; white-space: nowrap; }

  .hero { position: absolute; left: 0; top: 127px; width: 1200px; height: 382px; }
  .hero-photo { position: absolute; inset: 0; background: linear-gradient(100deg, #eef0f3 0%, #e3e6ea 35%, #cfd4db 55%, #5b6f8d 78%, #2e4468 100%); }
  .hero-band { position: absolute; left: 0; right: 0; bottom: 0; height: 86px; background: rgba(70,78,92,.55); }
  .hero-title { position: absolute; left: 89px; top: 320px; font-family: "Open Sans", Arial, sans-serif; font-weight: 600; font-size: 31px; color: var(--orange); text-shadow: 0 1px 2px rgba(0,0,0,.25); white-space: nowrap; }
  .cta { position: absolute; left: 859px; top: 313px; width: 250px; height: 52px; background: linear-gradient(var(--orange), var(--orange-dark)); border-radius: 3px; display: flex; align-items: center; padding-left: 18px; gap: 10px; font-family: "PT Sans Narrow", Arial, sans-serif; font-weight: 700; font-size: 25px; color: var(--white); box-shadow: 0 2px 4px rgba(0,0,0,.3); white-space: nowrap; }

  .features { position: absolute; left: 0; top: 509px; width: 1200px; height: 210px; background: linear-gradient(90deg, var(--peach) 0%, var(--peach-light) 50%, var(--peach) 100%); }
  .feature { position: absolute; top: 0; width: 296px; }
  .feature-title, .section-title { font-family: "PT Sans Narrow", Arial, sans-serif; font-size: 27px; color: var(--orange); font-weight: 700; white-space: nowrap; }
  .feature-title { margin-top: 25px; }
  .feature p { margin-top: 8px; font-size: 14px; line-height: 23px; color: var(--text); }
  .btn-read { display: inline-block; margin-top: 20px; width: 87px; height: 33px; line-height: 33px; text-align: center; background: var(--orange); color: var(--white); font-size: 14px; font-style: italic; border-radius: 2px; }

  .rule { position: absolute; left: 90px; top: 719px; width: 1021px; height: 1px; background: var(--rule); }

  .section { position: absolute; }
  .video { position: absolute; left: 92px; top: 778px; width: 300px; height: 201px; border-radius: 3px; background: linear-gradient(120deg, #d9dbe0 0%, #c5b9a9 50%, #9a9186 100%); }
  .video .play { position: absolute; left: 126px; top: 69px; }

  .quote { position: absolute; left: 460px; top: 803px; width: 285px; font-size: 15px; font-style: italic; line-height: 25px; text-align: justify; color: var(--text); }
  .quote-mark { font-family: Georgia, serif; font-size: 34px; font-style: normal; color: #777; line-height: 0; vertical-align: -12px; }
  .client { position: absolute; right: 471px; top: 991px; font-size: 15px; color: var(--text-dark); }

  .contact { position: absolute; left: 816px; top: 806px; font-size: 15px; line-height: 23px; color: var(--text-dark); }
  .contact p + p { margin-top: 6px; }
  .find { position: absolute; left: 1029px; top: 951px; font-size: 10px; color: #999; }

  .footer { position: absolute; left: 0; top: 1047px; width: 1200px; height: 102px; border-top: 3px solid var(--orange); background: linear-gradient(var(--footer-top), var(--footer)); }
  .footer-nav { position: absolute; left: 90px; top: 24px; font-size: 15px; color: var(--footer-text); }
  .footer-nav span { margin: 0 12px; }
  .copyright { position: absolute; left: 90px; top: 58px; font-size: 14px; color: var(--footer-text); }
  .social { position: absolute; top: 36px; width: 33px; height: 33px; border-radius: 3px; background: linear-gradient(#d4d4d4, #a9a9a9); }
</style>
</head>
<body>

<div class="search">Search
  <svg width="20" height="20" viewBox="0 0 20 20"><circle cx="8" cy="8" r="6" fill="none" stroke="#888" stroke-width="1.6"/><line x1="12.5" y1="12.5" x2="18" y2="18" stroke="#666" stroke-width="2.4" stroke-linecap="round"/></svg>
</div>

<div class="brand"><span class="brand-mark"></span><span class="brand-name">QUELLANE</span></div>

<nav class="main-nav">
  <a href="#" style="left:638px">Home</a>
  <a href="#" style="left:747px">About us</a>
  <a href="#" style="left:883px">Services</a>
  <a href="#" style="left:1012px">Contact us</a>
</nav>

<section class="hero">
  <div class="hero-photo" role="img" aria-label="Business team meeting around a conference table"></div>
  <div class="hero-band"></div>
  <h1 class="hero-title">Counsel for Business Deals</h1>
  <a class="cta" href="#">GET STARTED NOW
    <svg width="24" height="24" viewBox="0 0 24 24"><circle cx="12" cy="12" r="11" fill="#c9520a"/><path d="M10 7l5 5-5 5" fill="none" stroke="#fff" stroke-width="2.4"/></svg>
  </a>
</section>

<section class="features">
  <div class="feature" style="left:89px">
    <h2 class="feature-title">HEALTHCARE</h2>
    <p>Deals, compliance and regulatory advice for providers, payers and the investors who back them, handled quickly.</p>
    <a class="btn-read" href="#">Read more</a>
  </div>
  <div class="feature" style="left:452px">
    <h2 class="feature-title">MERGERS &amp; FINANCING</h2>
    <p>Acquisitions, sales and capital raises guided from term sheet to closing, as a working part of your business team.</p>
    <a class="btn-read" href="#">Read more</a>
  </div>
  <div class="feature" style="left:816px">
    <h2 class="feature-title">TECHNOLOGY</h2>
    <p>Licensing, procurement and productization for tech and internet companies that need to move fast and stay protected.</p>
    <a class="btn-read" href="#">Read more</a>
  </div>
</section>

<div class="rule"></div>

<h2 class="section section-title" style="left:94px; top:738px">HOW WE WORK</h2>
<div class="video" role="img" aria-label="Video still of attorneys meeting with clients">
  <svg class="play" width="58" height="58" viewBox="0 0 58 58"><circle cx="29" cy="29" r="29" fill="#2a2a2a"/><path d="M24 18l13 11-13 11z" fill="#fff"/></svg>
</div>

<h2 class="section section-title" style="left:455px; top:745px">TESTIMONIALS</h2>
<p class="quote"><span class="quote-mark">&ldquo;</span> Quellane worked as part of our own team through a complex acquisition. They spotted the regulatory issues early, kept the deal moving and explained every trade-off in plain business terms. We closed on schedule and with far less friction than we had expected from a law firm. <span class="quote-mark">&rdquo;</span></p>
<p class="client">Client name, City</p>

<h2 class="section section-title" style="left:816px; top:745px">CONTACT US</h2>
<div class="contact">
  <p>Address :<br>Quellane Law Firm, P.C.<br>8716 SW 19th Ave., Portland, OR 97213</p>
  <p>Call us : 971.555.0143</p>
  <p>Fax : 971.555.0187</p>
  <p>Email : info@quellane.example</p>
</div>
<a class="find" href="#">Find Location</a>

<footer class="footer">
  <nav class="footer-nav"><a href="#">Home</a><span>|</span><a href="#">About us</a><span>|</span><a href="#">Services</a><span>|</span><a href="#">Contact us</a></nav>
  <p class="copyright">Copyright &copy; 2014 QUELLANE. All Rights Reserved.</p>
  <a class="social" href="#" style="left:978px" aria-label="Social profile"></a>
  <a class="social" href="#" style="left:1028px" aria-label="Social profile"></a>
  <a class="social" href="#" style="left:1078px" aria-label="Social profile"></a>
</footer>

</body>
</html>
```